Vorniclean.net

This is a postcard for a Dry Cleaning Business .Please find attached the info I want to put in. Please use the pictures I attached . Keep the pictures on top
You can change the lay out of the bottom part as you see fit.
Keep the blue on the background for the bottom

Make the coupon 10% off to look better

This is the final layout .

Please make it look good I I will buy your design .

Target Market(s)

Up scale neighborhood

Industry/Entity Type

Business

Requirements
Must have
• Vornclean.net ( the company name ) should be in blue

```html
<!DOCTYPE html>
<html lang="en">
<head>
<meta charset="utf-8">
<title>Vornclean.net Postcard</title>
<link rel="stylesheet" href="https://fonts.googleapis.com/css2?family=Source+Sans+3:ital,wght@0,300;0,400;0,600;0,700;1,400&display=swap">
<style>
  :root {
    --stage: #e9e9ec;
    --paper: #ffffff;
    --stop-red: #e5202a;
    --navy: #262c6b;
    --ink: #111111;
    --teal: #2a9fb0;
    --teal-dark: #1a7f90;
    --teal-light: #7fd0da;
    --band-light: #ffffff;
    --band-blue: #c7d2ec;
    --logo-band: #f1f1f2;
  }
  * { box-sizing: border-box; margin: 0; padding: 0; }
  html, body { width: 857px; height: 1200px; overflow: hidden; }
  body {
    background: var(--stage);
    font-family: "Source Sans 3", Arial, sans-serif;
    position: relative;
  }
  .card {
    position: absolute;
    background: var(--paper);
    box-shadow: 0 4px 14px rgba(0,0,0,0.25);
    overflow: hidden;
  }
  .card--front { left: 78px; top: 73px; width: 656px; height: 508px; }
  .card--back { left: 150px; top: 614px; width: 656px; height: 510px; }

  /* front */
  .front-header { position: absolute; left: 0; top: 0; width: 100%; height: 97px; background: var(--paper); }
  .stop-sign { position: absolute; left: 49px; top: 6px; width: 96px; height: 88px; }
  .headline {
    position: absolute; left: 186px; top: 8px;
    font-size: 36px; font-weight: 400; color: var(--stop-red); line-height: 1;
  }
  .subline {
    position: absolute; left: 183px; top: 57px;
    font-size: 22px; font-weight: 700; color: var(--ink); line-height: 1;
  }
  .subline em { font-style: normal; color: var(--stop-red); }
  .front-photo {
    position: absolute; left: 0; top: 97px; width: 100%; height: 300px;
    background:
      radial-gradient(ellipse 90px 70px at 175px 40px, rgba(226,196,140,0.95), rgba(226,196,140,0) 100%),
      radial-gradient(ellipse 70px 60px at 230px 95px, rgba(236,206,186,0.9), rgba(236,206,186,0) 100%),
      radial-gradient(ellipse 220px 170px at 180px 250px, rgba(160,186,225,0.95), rgba(160,186,225,0) 100%),
      radial-gradient(ellipse 260px 60px at 470px 30px, rgba(118,140,110,0.75), rgba(118,140,110,0) 100%),
      radial-gradient(ellipse 60px 90px at 415px 110px, rgba(50,60,80,0.55), rgba(50,60,80,0) 100%),
      radial-gradient(ellipse 45px 80px at 510px 120px, rgba(120,130,150,0.5), rgba(120,130,150,0) 100%),
      radial-gradient(ellipse 220px 80px at 560px 150px, rgba(140,200,190,0.7), rgba(140,200,190,0) 100%),
      linear-gradient(to bottom, #c9d0cc 0%, #d9dcd8 45%, #cfc4b4 100%);
  }
  .brand {
    position: absolute; color: var(--navy); font-weight: 400; line-height: 1;
    display: flex; align-items: center; gap: 10px;
  }
  .brand__mark { width: 22px; height: 22px; background: var(--navy); }
  .card--front .brand { left: 24px; top: 357px; font-size: 32px; }
  .front-band {
    position: absolute; left: 0; top: 397px; width: 100%; height: 111px;
    background: linear-gradient(to bottom, var(--band-light) 0%, var(--band-blue) 100%);
  }
  .contact { position: absolute; color: var(--navy); font-size: 20px; line-height: 1; }
  .contact b { font-weight: 700; }
  .contact--call { display: flex; align-items: center; gap: 8px; }
  .phone-icon { width: 22px; height: 22px; }
  .perks { position: absolute; font-style: italic; font-size: 14.5px; color: var(--ink); line-height: 1.45; }
  .card--front .contact--web { left: 23px; top: 413px; }
  .card--front .contact--call { left: 23px; top: 440px; }
  .card--front .perks { left: 20px; top: 472px; }

  .coupon { position: absolute; left: 356px; top: 344px; width: 290px; height: 140px; }
  .coupon__text {
    position: absolute; left: 438px; top: 366px; width: 200px;
    text-align: center; color: var(--navy); line-height: 1;
  }
  .coupon__lead { font-size: 13px; text-transform: uppercase; line-height: 1.1; }
  .coupon__value { font-size: 34px; font-weight: 700; color: #fff; margin: 3px 0 1px; }
  .coupon__value small { font-size: 21px; font-weight: 700; }
  .coupon__tail { font-size: 13px; text-transform: uppercase; }

  /* back */
  .back-panel { position: absolute; left: 0; top: 0; width: 414px; height: 378px; }
  .back-photo {
    position: absolute; left: 0; top: 0; width: 100%; height: 155px;
    background:
      radial-gradient(ellipse 40px 110px at 235px 90px, rgba(25,25,30,0.85), rgba(25,25,30,0) 100%),
      radial-gradient(ellipse 85px 120px at 230px 110px, rgba(140,140,142,0.95), rgba(140,140,142,0) 100%),
      radial-gradient(ellipse 70px 90px at 140px 110px, rgba(245,245,248,0.95), rgba(245,245,248,0) 100%),
      radial-gradient(ellipse 90px 110px at 330px 100px, rgba(120,118,120,0.85), rgba(120,118,120,0) 100%),
      radial-gradient(ellipse 30px 30px at 268px 95px, rgba(180,120,100,0.7), rgba(180,120,100,0) 100%),
      linear-gradient(to bottom, #d8d8da 0%, #d8d8da 12%, rgba(216,216,218,0) 22%),
      linear-gradient(90deg, #2b2d33 0%, #3a3c44 25%, #6d6e74 45%, #55565c 75%, #2f3035 100%);
  }
  .back-logo-band { position: absolute; left: 0; top: 155px; width: 100%; height: 70px; background: var(--logo-band); }
  .card--back .brand { left: 49px; top: 174px; font-size: 33px; }
  .card--back .contact--web { left: 46px; top: 250px; }
  .card--back .contact--call { left: 46px; top: 278px; }
  .back-band {
    position: absolute; left: 0; top: 313px; width: 100%; height: 65px;
    background: linear-gradient(to bottom, var(--band-light) 0%, var(--band-blue) 100%);
  }
  .card--back .perks { left: 40px; top: 324px; }
  .card--back .perks span { display: block; }
  .card--back .perks span + span { padding-left: 80px; }
</style>
</head>
<body>

<section class="card card--front">
  <header class="front-header">
    <svg class="stop-sign" viewBox="0 0 100 100" aria-hidden="true">
      <polygon points="30,2 70,2 98,30 98,70 70,98 30,98 2,70 2,30" fill="#fff" stroke="#ccc" stroke-width="1"/>
      <polygon points="31,6 69,6 94,31 94,69 69,94 31,94 6,69 6,31" fill="var(--stop-red)"/>
      <text x="50" y="60" text-anchor="middle" font-family="Arial, sans-serif" font-weight="700" font-size="28" fill="#fff">STOP</text>
    </svg>
    <h1 class="headline">STOP driving around !</h1>
    <p class="subline">Your dry-cleaning service is <em>ONE CLICK</em> away</p>
  </header>

  <div class="front-photo" role="img" aria-label="Photo: smiling woman carrying freshly cleaned shirts in a plastic bag on a city street"></div>

  <div class="brand"><span class="brand__mark"></span>Vornclean.net</div>

  <div class="front-band"></div>
  <p class="contact contact--web">Sign up today : <b>www.vornclean.net</b></p>
  <p class="contact contact--call">or Call
    <svg class="phone-icon" viewBox="0 0 24 24" aria-hidden="true"><circle cx="12" cy="12" r="10.5" fill="none" stroke="var(--navy)" stroke-width="1.6"/><path d="M8.5 6.5l2 2-1 1.5c.6 1.6 2 3 3.5 3.5l1.5-1 2 2-1.3 1.8c-3.8-.3-7.2-3.7-7.5-7.5z" fill="var(--navy)"/></svg>
    <b>555 014 2290</b></p>
  <p class="perks">LATE HOURS&nbsp; free pick up &amp; delivery ( up to 10 PM !!) &nbsp;&nbsp; 24 HOURS&nbsp; turnaround</p>

  <svg class="coupon" viewBox="0 0 290 140" aria-hidden="true">
    <defs>
      <linearGradient id="tagFill" x1="0" y1="0" x2="1" y2="1">
        <stop offset="0" stop-color="var(--teal-dark)"/>
        <stop offset="0.55" stop-color="var(--teal)"/>
        <stop offset="1" stop-color="var(--teal-light)"/>
      </linearGradient>
    </defs>
    <path d="M14 36 C 4 14, 50 10, 66 68" fill="none" stroke="#666" stroke-width="2"/>
    <path d="M44 72 L 84 24 Q 89 18 98 18 L 270 16 Q 284 16 284 30 L 284 114 Q 284 128 270 128 L 98 130 Q 89 130 84 124 Z" fill="#9aa3b3" opacity="0.55" transform="translate(4,6)"/>
    <path d="M44 72 L 84 24 Q 89 18 98 18 L 270 16 Q 284 16 284 30 L 284 114 Q 284 128 270 128 L 98 130 Q 89 130 84 124 Z" fill="url(#tagFill)"/>
    <circle cx="66" cy="72" r="6" fill="#fff" stroke="#888" stroke-width="1.5"/>
  </svg>
  <div class="coupon__text">
    <p class="coupon__lead">Sign up this week<br>to receive</p>
    <p class="coupon__value">10 % <small>off</small></p>
    <p class="coupon__tail">For the next&nbsp; 3 months</p>
  </div>
</section>

<section class="card card--back">
  <div class="back-panel">
    <div class="back-photo" role="img" aria-label="Photo: man in a grey vest holding a jacket over his shoulder in front of a rack of suits"></div>
    <div class="back-logo-band"></div>
    <div class="brand"><span class="brand__mark"></span>Vornclean.net</div>
    <p class="contact contact--web">Sign up today : <b>www.vornclean.net</b></p>
    <p class="contact contact--call">or Call
      <svg class="phone-icon" viewBox="0 0 24 24" aria-hidden="true"><circle cx="12" cy="12" r="10.5" fill="none" stroke="var(--navy)" stroke-width="1.6"/><path d="M8.5 6.5l2 2-1 1.5c.6 1.6 2 3 3.5 3.5l1.5-1 2 2-1.3 1.8c-3.8-.3-7.2-3.7-7.5-7.5z" fill="var(--navy)"/></svg>
      <b>555 014 2290</b></p>
    <div class="back-band"></div>
    <p class="perks"><span>LATE HOURS&nbsp; free pick up &amp; delivery ( up to 10 PM !!)</span><span>24 HOURS&nbsp; turnaround</span></p>
  </div>
</section>

</body>
</html>
```